Product Packaging design for Vaporizer Battery box

We are looking for product packaging for a new line of Vaporizer Batteries. These batteries are all sold in bundle packs, and each battery has its own cardboard box. For example, the bundle packs are simply bagged up packs of 2, 3, 5, 10, 25, etc.

There are 4 different kinds of batteries that we need the packaging designed for. I have attached templates of the packaging for your reference. I would like the packaging to be a similar theme across all the batteries to keep things consistent.

More details about the 4 batteries can be found on our website at:
http://www.tindrelcoilworks.com/product-category/vape_batteries/
Password: tindrelvisit

Packing Requirements

The packaging should have our company logo somewhere on it. I have attached a few different variations/orientations of our logo for you to choose between.

The name of the battery
Tindrel Goods 1300mAh Variable Voltage Large Capacity Battery
Tindrel Goods 400mAh Slim Variable Voltage Battery
Tindrel Goods 280mAh Slim Automatic Buttonless Battery
Tindrel Goods 350mAh KOV Slim Battery

Company website www.TindrelCoilworks.com

For the Tindrel Goods 350mAh KOV Slim Battery, have the product packaging color scheme be Black base with Gold wording/trim. This battery only comes in black and gold, so the packaging will match.

Make sure to use the proper packaging template for the batteries. There are only two templates and pretty much the only difference is the size. They both fold up to be a rectangle package.

Industry/Entity Type

Product

Colors

Designer to choose colors to be used in the design.

Requirements
Must have
• Packing Requirements
• The packaging should have our company logo somewhere on it. I have attached a few different variations/orientations of our logo for you to choose between.
• The name of the battery
• Tindrel Goods 1300mAh Variable Voltage Large Capacity Battery
• Tindrel Goods 400mAh Slim Variable Voltage Battery
• Tindrel Goods 280mAh Slim Automatic Buttonless Battery
• Tindrel Goods 350mAh KOV Slim Battery
• Company website www.TindrelCoilworks.com
• For the Tindrel Goods 350mAh KOV Slim Battery, have the product packaging color scheme be Black base with Gold wording/trim. This battery only comes in black and gold, so the packaging will match.
• Make sure to use the proper packaging template for the batteries. There are only two templates and pretty much the only difference is the size. They both fold up to be a rectangle package.

```html
<!DOCTYPE html>
<html lang="en">
<head>
<meta charset="utf-8">
<title>Tindrel Goods – Battery Box Dielines</title>
<link rel="stylesheet" href="https://fonts.googleapis.com/css2?family=Saira:wght@500;600&display=swap">
<style>
  :root {
    --paper: #ffffff;
    --board: #0b0b0b;
    --crease: #3a3a3a;
    --gold: #c9a06a;
    --red: #e2302a;
    --teal: #16a39a;
    --pink: #e0197a;
    --ink: #0b0b0b;
  }
  html, body {
    margin: 0;
    padding: 0;
    width: 1200px;
    height: 848px;
    overflow: hidden;
    background: var(--paper);
  }
  .sheet { display: block; width: 1200px; height: 848px; }
  .board { fill: var(--board); }
  .crease { stroke: var(--crease); stroke-width: 1; fill: none; }
  .accent-fill { fill: var(--accent); }
  .band-label {
    fill: var(--ink);
    font-family: "Saira", sans-serif;
    font-weight: 600;
    font-size: 13px;
    letter-spacing: 0.5px;
  }
  .band-sub {
    fill: var(--ink);
    font-family: "Saira", sans-serif;
    font-weight: 600;
    font-size: 6px;
    letter-spacing: 3px;
  }
  .tab-label {
    fill: var(--accent);
    font-family: "Saira", sans-serif;
    font-weight: 600;
    font-size: 13px;
    letter-spacing: 1px;
  }
  .product-name {
    fill: var(--accent);
    font-family: "Saira", sans-serif;
    font-weight: 500;
    font-size: 17px;
  }
  .product-name.long { font-size: 15.5px; }
  .box-kov { --accent: var(--gold); }
  .box-1300 { --accent: var(--red); }
  .box-400 { --accent: var(--teal); }
  .box-280 { --accent: var(--pink); }
</style>
</head>
<body>
<svg class="sheet" viewBox="0 0 1500 1060" width="1200" height="848" xmlns="http://www.w3.org/2000/svg" xmlns:xlink="http://www.w3.org/1999/xlink">
  <defs>
    <g id="band-mark">
      <text class="band-label" transform="translate(555 0) rotate(90)" text-anchor="middle" dominant-baseline="middle">TINDREL</text>
      <text class="band-sub" transform="translate(541 1.5) rotate(90)" text-anchor="middle" dominant-baseline="middle">GOODS</text>
      <rect x="576" y="-12" width="24" height="24" fill="var(--ink)"/>
    </g>
    <g id="box-shell">
      <polygon class="board" points="168,193 174,168 646,168 648,193"/>
      <path class="board" d="M168,194 H81 a8,8 0 0 0 -8,8 V262 a8,8 0 0 0 8,8 H168 Z"/>
      <polygon class="board" points="168,271 132,275 128,345 168,345"/>
      <polygon class="board" points="168,421 132,425 128,497 168,497"/>
      <polygon class="board" points="648,271 686,275 688,345 648,345"/>
      <polygon class="board" points="648,421 686,425 688,497 648,497"/>
      <path class="board" d="M648,345 H737 a8,8 0 0 1 8,8 V412 a8,8 0 0 1 -8,8 H648 Z"/>
      <rect class="board" x="168" y="193" width="480" height="304"/>
      <rect class="accent-fill" x="521" y="168" width="100" height="329"/>
      <line class="crease" x1="168" y1="193" x2="521" y2="193"/>
      <line class="crease" x1="621" y1="193" x2="648" y2="193"/>
      <line class="crease" x1="168" y1="270" x2="521" y2="270"/>
      <line class="crease" x1="621" y1="270" x2="648" y2="270"/>
      <line class="crease" x1="168" y1="345" x2="521" y2="345"/>
      <line class="crease" x1="621" y1="345" x2="648" y2="345"/>
      <line class="crease" x1="168" y1="420" x2="521" y2="420"/>
      <line class="crease" x1="621" y1="420" x2="648" y2="420"/>
      <line class="crease" x1="168" y1="193" x2="168" y2="497"/>
      <line class="crease" x1="648" y1="193" x2="648" y2="497"/>
      <use xlink:href="#band-mark" transform="translate(0 231)"/>
      <use xlink:href="#band-mark" transform="translate(0 307)"/>
      <use xlink:href="#band-mark" transform="translate(0 382)"/>
      <use xlink:href="#band-mark" transform="translate(0 458)"/>
      <text class="tab-label" x="121" y="232" text-anchor="middle" dominant-baseline="middle">TINDREL</text>
      <text class="tab-label" x="697" y="383" text-anchor="middle" dominant-baseline="middle">TINDREL</text>
      <g class="compliance">
        <rect class="accent-fill" x="198" y="369" width="34" height="26" rx="4"/>
        <circle class="accent-fill" cx="265" cy="382" r="20"/>
        <circle class="accent-fill" cx="313" cy="382" r="17"/>
        <rect class="accent-fill" x="340" y="362" width="30" height="44" rx="2"/>
      </g>
    </g>
  </defs>

  <g class="box-kov">
    <use xlink:href="#box-shell"/>
    <text class="product-name" x="200" y="224">350mAh</text>
    <text class="product-name" x="200" y="246">KOV Slim Battery</text>
    <text class="product-name" x="200" y="304">350mAh</text>
    <text class="product-name" x="200" y="326">KOV Slim Battery</text>
    <text class="product-name" x="200" y="455">350mAh</text>
    <text class="product-name" x="200" y="477">KOV Slim Battery</text>
  </g>

  <g class="box-1300" transform="translate(683 0)">
    <use xlink:href="#box-shell"/>
    <text class="product-name" x="200" y="224">1300mAh</text>
    <text class="product-name long" x="200" y="244">Variable Voltage Large Capacity Battery</text>
    <text class="product-name" x="200" y="304">1300mAh</text>
    <text class="product-name long" x="200" y="324">Variable Voltage Large Capacity Battery</text>
    <text class="product-name" x="200" y="455">1300mAh</text>
    <text class="product-name long" x="200" y="475">Variable Voltage Large Capacity Battery</text>
  </g>

  <g class="box-400" transform="translate(0 397)">
    <use xlink:href="#box-shell"/>
    <text class="product-name" x="200" y="224">400mAh</text>
    <text class="product-name" x="200" y="246">Slim Variable Voltage Battery</text>
    <text class="product-name" x="200" y="304">400mAh</text>
    <text class="product-name" x="200" y="326">Slim Variable Voltage Battery</text>
    <text class="product-name" x="200" y="455">400mAh</text>
    <text class="product-name" x="200" y="477">Slim Variable Voltage Battery</text>
  </g>

  <g class="box-280" transform="translate(683 397)">
    <use xlink:href="#box-shell"/>
    <text class="product-name" x="200" y="224">280mAh</text>
    <text class="product-name" x="200" y="246">Slim Automatic Buttonless Battery</text>
    <text class="product-name" x="200" y="304">280mAh</text>
    <text class="product-name" x="200" y="326">Slim Automatic Buttonless Battery</text>
    <text class="product-name" x="200" y="455">280mAh</text>
    <text class="product-name" x="200" y="477">Slim Automatic Buttonless Battery</text>
  </g>
</svg>
</body>
</html>
```